Steady Harbor Claims Group Business card

Need a business card that stands out that includes name of company,(above) Owners name Moira Lindqvist phone#517-362-4408 email# SteadyHarborCG@mailvane.com and website www.Steadyharborclaimsgroup.net. This is a medical billing company so the card has to relate to that or relate to increasing revenue

```html
<!DOCTYPE html>
<html lang="en">
<head>
<meta charset="utf-8">
<title>Steady Harbor Claims Group — Business Card</title>
<link rel="stylesheet" href="https://fonts.googleapis.com/css2?family=Cinzel:wght@600&family=Montserrat:wght@600&family=Roboto:ital,wght@0,400;1,400&display=swap">
<style>
  :root {
    --backdrop: #a8a6a6;
    --card-blue: #11549a;
    --card-white: #f6f6f4;
    --ink-blue: #17488a;
    --link-blue: #2f6fb8;
    --accent-green: #7cbd2c;
    --rule-blue: #3b86cf;
    --white: #ffffff;
    --ghost-light: rgba(255, 255, 255, 0.07);
    --ghost-dark: rgba(23, 72, 138, 0.06);
  }
  * { margin: 0; padding: 0; box-sizing: border-box; }
  html, body { width: 1200px; height: 1200px; overflow: hidden; }
  body { background: var(--backdrop); position: relative; font-family: "Roboto", Arial, sans-serif; }

  .card { position: absolute; width: 713px; height: 418px; overflow: hidden; }
  .card--front { left: 238px; top: 118px; background: var(--card-blue); }
  .card--back { left: 230px; top: 645px; background: var(--card-white); }

  .ghost-mark { position: absolute; border-radius: 50%; }
  .card--front .ghost-mark { left: -90px; top: 90px; width: 360px; height: 360px; background: var(--ghost-light); }
  .card--back .ghost-mark { left: -110px; top: 40px; width: 360px; height: 360px; background: var(--ghost-dark); }

  .brand-mark { position: absolute; background: var(--accent-green); }
  .card--front .brand-mark { left: 308px; top: 110px; width: 96px; height: 96px; border-radius: 50%; }
  .card--back .brand-mark { left: 100px; top: 72px; width: 100px; height: 100px; }

  .brand-name {
    position: absolute;
    font-family: "Cinzel", "Times New Roman", serif;
    font-weight: 600;
    line-height: 31px;
    letter-spacing: 0.6px;
  }
  .card--front .brand-name { left: 0; width: 100%; top: 234px; text-align: center; font-size: 30px; color: var(--white); }
  .card--back .brand-name { left: 252px; top: 90px; font-size: 30px; color: var(--ink-blue); }

  .person { position: absolute; left: 0; width: 100%; top: 212px; text-align: center; }
  .person__name { font-family: "Montserrat", Arial, sans-serif; font-weight: 600; font-size: 26px; color: var(--ink-blue); letter-spacing: 0.3px; }
  .person__role { display: flex; align-items: center; justify-content: center; gap: 14px; margin-top: 8px; }
  .person__rule { width: 220px; height: 2px; background: linear-gradient(90deg, transparent, var(--rule-blue) 15%, var(--rule-blue) 85%, transparent); }
  .person__title { font-style: italic; font-size: 15px; color: var(--accent-green); width: 90px; }

  .contact { position: absolute; left: 0; width: 716px; top: 294px; text-align: center; font-size: 18px; line-height: 28px; color: var(--ink-blue); }
  .contact__domain { color: var(--link-blue); }
</style>
</head>
<body>
  <section class="card card--front" aria-label="Card front">
    <span class="ghost-mark" role="img" aria-label="Faint enlarged brand symbol"></span>
    <span class="brand-mark"></span>
    <div class="brand-name">Steady Harbor<br>Claims Group</div>
  </section>

  <section class="card card--back" aria-label="Card back">
    <span class="ghost-mark" role="img" aria-label="Faint enlarged brand symbol"></span>
    <span class="brand-mark"></span>
    <div class="brand-name">Steady Harbor<br>Claims Group</div>
    <div class="person">
      <div class="person__name">Moira Lindqvist</div>
      <div class="person__role">
        <span class="person__rule"></span>
        <span class="person__title">Owner</span>
        <span class="person__rule"></span>
      </div>
    </div>
    <div class="contact">
      <div>517-362-4408</div>
      <div>SteadyHarborCG@mailvane.com</div>
      <div>www.<span class="contact__domain">Steadyharborclaimsgroup</span>.net</div>
    </div>
  </section>
</body>
</html>
```